Stone Arch Letterhead

I just need letterhead for my integrative psychiatry business. I'm going to use this to do mailings to other doctors, as well as send letters to patients. Thank you

```html
<!DOCTYPE html>
<html lang="en">
<head>
<meta charset="utf-8">
<title>Stone Arch Letterhead</title>
<link href="https://fonts.googleapis.com/css2?family=Arimo:wght@400;700&display=swap" rel="stylesheet">
<style>
:root{
  --green:#0d9640;
  --green-soft:#17a84c;
  --green-text:#16963f;
  --ink:#1a1a1a;
  --body:#333333;
  --brand:#2f6b1f;
  --paper:#ffffff;
  --canvas:#ffffff;
  --leaf-grey:#e4e4e4;
  --shadow:rgba(0,0,0,.35);
}
*{margin:0;padding:0;box-sizing:border-box}
html,body{width:1200px;height:1000px;overflow:hidden;background:var(--canvas)}
body{position:relative;font-family:"Arimo",Arial,sans-serif;color:var(--ink)}
.sheet{position:absolute;background:var(--paper);box-shadow:3px 4px 6px var(--shadow)}

/* Folder */
.folder{left:10px;top:25px;width:570px;height:740px;overflow:hidden}
.folder-band{position:absolute;top:0;height:100%;background:var(--green)}
.folder-band--left{left:0;width:227px}
.folder-band--right{left:522px;width:48px}
.folder-foliage{position:absolute;inset:0;background:radial-gradient(ellipse at 60% 45%,var(--green-soft) 0%,rgba(23,168,76,.5) 45%,rgba(13,150,64,0) 75%)}

/* Brand lockup */
.brand{position:absolute;display:flex;flex-direction:column;align-items:center}
.brand-mark{display:flex;align-items:center;gap:8px}
.brand-dot{width:14px;height:14px;border-radius:50%;background:var(--brand)}
.brand-name{font-weight:700;color:var(--brand)}
.brand-tagline{color:var(--ink);margin-top:10px}
.folder .brand{left:227px;width:295px;top:500px}
.folder .brand-name{font-size:26px}
.folder .brand-tagline{font-size:11px;margin-top:26px}

/* Letterhead */
.letterhead{left:583px;top:28px;width:585px;height:740px;overflow:hidden}
.foliage{position:absolute;background:radial-gradient(ellipse at center,var(--leaf-grey) 0%,rgba(228,228,228,.6) 50%,rgba(228,228,228,0) 78%)}
.letterhead .foliage--top{left:300px;top:-20px;width:320px;height:300px}
.letterhead .foliage--bottom{left:230px;top:460px;width:400px;height:300px}
.credentials{position:absolute;right:15px;text-align:right}
.credentials-name{color:var(--green-text);font-weight:700}
.credentials-board{font-weight:700;color:var(--ink)}
.letterhead .credentials{top:32px}
.letterhead .credentials-name{font-size:13px;line-height:15px}
.letterhead .credentials-board{font-size:11px;line-height:14px}
.letterhead .brand{left:50px;top:125px;width:220px;align-items:flex-start}
.letterhead .brand-mark{margin-left:22px}
.letterhead .brand-name{font-size:24px}
.letterhead .brand-tagline{font-size:11px;margin-top:34px}
.letter{position:absolute;left:51px;top:258px;width:520px;font-size:11px;line-height:10.8px;color:var(--body)}
.letter-salutation{margin-bottom:32px}
.letter p{margin-bottom:11px}
.signoff{position:absolute;left:51px;top:526px;font-size:12px;line-height:29px;color:var(--body)}

/* Contact footer */
.contact{position:absolute;display:flex;align-items:flex-start;font-weight:700;color:var(--ink)}
.contact-item{border-left:3px solid var(--green);padding-left:12px}
.contact-item:first-child{border-left:none;padding-left:0}
.letterhead .contact{left:42px;top:656px;font-size:12px;line-height:15px}
.letterhead .contact-address{width:158px}
.letterhead .contact-phone{width:140px;padding-left:30px;padding-top:8px}
.letterhead .contact-web{padding-left:14px;padding-top:13px}

/* Compliment slip */
.slip{left:40px;top:732px;width:574px;height:253px}
.slip .brand{left:18px;top:18px;align-items:flex-start}
.slip .brand-dot{width:8px;height:8px}
.slip .brand-name{font-size:13px}
.slip .brand-tagline{font-size:6px;margin-top:26px}
.slip .credentials{top:27px;right:15px}
.slip .credentials-name{font-size:12px;line-height:15px}
.slip .credentials-board{font-size:10px;line-height:13px}
.slip .contact{left:22px;top:198px;font-size:10px;line-height:12px}
.slip .contact-item{border-left:2px solid var(--green);height:44px;padding-top:3px}
.slip .contact-item:first-child{border-left:2px solid var(--green);padding-left:11px;width:123px}
.slip .contact-phone{width:82px;padding-left:9px;padding-top:8px !important}
.slip .contact-web{width:180px;padding-left:8px;padding-top:15px !important}
.slip .contact-compliments{padding-left:11px;padding-top:14px !important;font-weight:400;color:var(--green-text);font-size:11px}
</style>
</head>
<body>

<section class="sheet folder" aria-label="Presentation folder">
  <div class="folder-band folder-band--left">
    <div class="folder-foliage" role="img" aria-label="Faint leaf pattern in lighter green"></div>
  </div>
  <div class="folder-band folder-band--right">
    <div class="folder-foliage" role="img" aria-label="Faint leaf pattern in lighter green"></div>
  </div>
  <div class="brand">
    <div class="brand-mark"><span class="brand-dot"></span><span class="brand-name">Stone Arch</span></div>
    <div class="brand-tagline">A Professional Medical Corporation</div>
  </div>
</section>

<section class="sheet letterhead" aria-label="Letterhead">
  <div class="foliage foliage--top" role="img" aria-label="Faint grey leaf decoration"></div>
  <div class="foliage foliage--bottom" role="img" aria-label="Faint grey leaf decoration"></div>

  <div class="credentials">
    <div class="credentials-name">Corinne Vasquel, MD</div>
    <div class="credentials-board">Diplomat, National Council of Mind and Brain Medicine</div>
    <div class="credentials-board">Diplomat, National Council of Integrative and Whole-Person Care</div>
  </div>

  <div class="brand">
    <div class="brand-mark"><span class="brand-dot"></span><span class="brand-name">Stone Arch</span></div>
    <div class="brand-tagline">A Professional Medical Corporation</div>
  </div>

  <div class="letter">
    <div class="letter-salutation">Dear Sir,</div>
    <p>Lorem Ipsum is simply dummy text of the printing and typesetting industry. Lorem Ipsum has been the industry's standard dummy text ever since the 1500s, when an unknown printer took a galley of type and scrambled it to make a type specimen book. It has survived not only five centuries, but also the leap into electronic typesetting, remaining essentially unchanged. It was popularised in the 1960s with the release of transfer sheets containing Lorem Ipsum passages, and more recently with desktop layout tools including versions of Lorem Ipsum.</p>
    <p>It is a long established fact that a reader will be distracted by the readable content of a page when looking at its layout. The point of using Lorem Ipsum is that it has a more-or-less normal distribution of letters, as opposed to using 'Content here, content here', making it look like readable English. Many desktop publishing packages and web page editors now use Lorem Ipsum as their default model text, and a search for 'lorem ipsum' will uncover many web sites still in their infancy. Various versions have evolved over the years, sometimes by accident, sometimes on purpose (injected humour and the like).</p>
  </div>

  <div class="signoff">
    <div>Your Name</div>
    <div>Company Name</div>
  </div>

  <div class="contact">
    <div class="contact-item contact-address">2870 Alder Creek Road<br>Suite 210<br>Fair Oaks, CA 95628</div>
    <div class="contact-item contact-phone">555-014-2286<br>555-014-2287</div>
    <div class="contact-item contact-web">www.stonearchwellness.com</div>
  </div>
</section>

<section class="sheet slip" aria-label="Compliment slip">
  <div class="brand">
    <div class="brand-mark"><span class="brand-dot"></span><span class="brand-name">Stone Arch</span></div>
    <div class="brand-tagline">A Professional Medical Corporation</div>
  </div>

  <div class="credentials">
    <div class="credentials-name">Corinne Vasquel, MD</div>
    <div class="credentials-board">Diplomat, National Council of Mind and Brain Medicine</div>
    <div class="credentials-board">Diplomat, National Council of Integrative and Whole-Person Care</div>
  </div>

  <div class="contact">
    <div class="contact-item contact-address">2870 Alder Creek Road<br>Suite 210<br>Fair Oaks, CA 95628</div>
    <div class="contact-item contact-phone">555-014-2286<br>555-014-2287</div>
    <div class="contact-item contact-web">www.stonearchwellness.com</div>
    <div class="contact-item contact-compliments">with best compliments</div>
  </div>
</section>

</body>
</html>
```